Re Brand for Australian health food company

We have are looking to revamp our brand including the look of our packaging. We use vertical Doy packs - Kraft Paper - Dimension of pack for fruit and berry products is 125mm W x 210mm H
Our chocolate coated products are packed in bags 125mm W x 170mm H
We are looking for natural, moderns simplistic packaging. We would like a see-through window on the front of ALL PACKAGING. The window should occupy approx 30% to 40% of the entire front of package. Designers need to consider that the existing Mxvitalbites logo can be modified slightly - but we DO NOT need a new logo. Designers also need to understand that the aesthetic must be able to be applied to all marketing materials - business cards, company letter head, e mail signatures, advertisements, fliers , our new web site (yet to be designed) and social media web sites.

Target Market(s)

Health conscious consumers, families, hipsters, athletes

Font styles to use
Serif
Sans Serif

Colors
87cfc6
85cae6
cadf82
fbf289
f59195
fbc994

Requirements
Must have
• Our existing company logo (can be modified)
• Product name - see our web site for all products - no names will be changed
• Ingredients
• Vegan friendly logo or clearly stated
• No preservatives
• No added sugar
Nice to have
• Clean, crisp modern font.
• Printing both sides f bags (rear of bags contains information associated with food products.
Should not have
• High gloss or reflective look.

```html
<!DOCTYPE html>
<html lang="en">
<head>
<meta charset="utf-8">
<title>Organic Dry Fruits – Pouch Front</title>
<link rel="stylesheet" href="https://fonts.googleapis.com/css2?family=Oswald:wght@400;500;600&display=swap">
<style>
  :root {
    --backdrop: #757575;
    --kraft: #cfae82;
    --kraft-deep: #bf9c6f;
    --teal: #87cfc6;
    --sky: #85cae6;
    --lime: #cadf82;
    --lemon: #fbf289;
    --rose: #f59195;
    --peach: #fbc994;
    --teal-ink: #1f5f58;
    --rose-ink: #b3404a;
    --olive-ink: #3b4a16;
    --ink: #2a2118;
    --nut-light: #d3a46c;
    --nut-mid: #9a5a32;
    --pistachio: #93a94a;
  }
  html, body {
    margin: 0;
    width: 1200px;
    height: 945px;
    overflow: hidden;
    background: var(--backdrop);
    font-family: "Oswald", sans-serif;
  }
  .pouch-front {
    position: absolute;
    left: 388px;
    top: 100px;
    width: 404px;
    height: 724px;
    background: linear-gradient(160deg, var(--kraft) 0%, var(--kraft-deep) 100%);
  }
  .brand-tab {
    position: absolute;
    left: 106px;
    top: 0;
    width: 198px;
    height: 184px;
  }
  .brand-name {
    position: absolute;
    left: 106px;
    top: 74px;
    width: 198px;
    text-align: center;
    color: var(--teal-ink);
    font-weight: 500;
    font-size: 30px;
    line-height: 1.2;
    letter-spacing: 0.5px;
  }
  .title {
    position: absolute;
    left: 0;
    width: 100%;
    margin: 0;
    text-align: center;
    font-weight: 600;
    font-size: 50px;
    line-height: 1;
    letter-spacing: 2px;
  }
  .title-organic { top: 196px; color: var(--teal-ink); }
  .title-product { top: 254px; color: var(--rose-ink); }
  .claim-ribbon {
    position: absolute;
    left: 80px;
    top: 322px;
    width: 248px;
    height: 46px;
  }
  .claim-text {
    position: absolute;
    left: 80px;
    top: 322px;
    width: 248px;
    height: 36px;
    line-height: 36px;
    text-align: center;
    color: var(--olive-ink);
    font-weight: 500;
    font-size: 22px;
    letter-spacing: 1px;
  }
  .diet-badge {
    position: absolute;
    top: 386px;
    width: 62px;
    text-align: center;
    color: var(--ink);
    font-weight: 500;
  }
  .diet-badge .mark {
    width: 34px;
    height: 34px;
    margin: 0 auto 4px;
    border-radius: 50%;
    font-size: 15px;
    line-height: 34px;
  }
  .diet-badge .label { font-size: 13px; line-height: 1.1; }
  .badge-gluten { left: 6px; }
  .badge-gluten .mark { background: var(--sky); }
  .badge-vegan { right: 6px; }
  .badge-vegan .mark { background: var(--lime); }
  .product-window {
    position: absolute;
    left: 72px;
    top: 378px;
    width: 260px;
    height: 260px;
    border-radius: 50%;
    box-sizing: border-box;
    border: 4px solid var(--lemon);
    background: radial-gradient(circle at 40% 40%, var(--nut-light), var(--nut-mid) 55%, var(--pistachio) 100%);
  }
  .descriptor {
    position: absolute;
    left: 0;
    top: 644px;
    width: 100%;
    margin: 0;
    text-align: center;
    color: var(--ink);
    font-weight: 500;
    font-size: 20px;
    line-height: 1.2;
    letter-spacing: 0.5px;
  }
  .free-from {
    position: absolute;
    left: 0;
    top: 670px;
    width: 100%;
    margin: 0;
    text-align: center;
    color: var(--rose-ink);
    font-weight: 500;
    font-size: 13px;
    line-height: 1.2;
    letter-spacing: 1px;
  }
  .net-weight {
    position: absolute;
    left: 138px;
    top: 690px;
    width: 128px;
    height: 26px;
  }
  .net-weight-text {
    position: absolute;
    left: 138px;
    top: 690px;
    width: 128px;
    height: 26px;
    line-height: 26px;
    text-align: center;
    color: var(--ink);
    font-size: 13px;
    font-weight: 500;
  }
</style>
</head>
<body>
  <main class="pouch-front">
    <svg class="brand-tab" viewBox="0 0 198 184" aria-hidden="true">
      <path d="M2 0 V88 A97 92 0 0 0 196 88 V0" fill="var(--teal)" stroke="var(--rose)" stroke-width="3"/>
    </svg>
    <div class="brand-name">Mxvitalbites</div>

    <h1 class="title title-organic">ORGANIC</h1>
    <h2 class="title title-product">DRY FRUITS</h2>

    <svg class="claim-ribbon" viewBox="0 0 248 46" aria-hidden="true">
      <polygon points="0,14 16,14 16,46 8,40 0,46" fill="var(--pistachio)"/>
      <polygon points="232,14 248,14 248,46 240,40 232,46" fill="var(--pistachio)"/>
      <polygon points="8,0 240,0 240,36 8,36" fill="var(--lime)"/>
    </svg>
    <div class="claim-text">100% NATURAL</div>

    <div class="diet-badge badge-gluten">
      <div class="mark">GF</div>
      <div class="label">GLUTEN<br>FREE</div>
    </div>
    <div class="diet-badge badge-vegan">
      <div class="mark">V</div>
      <div class="label">VEGAN<br>FRIENDLY</div>
    </div>

    <div class="product-window" role="img" aria-label="See-through window showing mixed almonds, pistachios, walnuts, hazelnuts and cashews"></div>

    <p class="descriptor">DRIED FRUITS AND NUTS</p>
    <p class="free-from">NO PRESERVATIVES · NO ADDED SUGAR</p>

    <svg class="net-weight" viewBox="0 0 128 26" aria-hidden="true">
      <polygon points="6,2 128,0 120,13 126,26 0,24 8,13" fill="var(--peach)"/>
    </svg>
    <div class="net-weight-text">NET WT. - 150G</div>
  </main>
</body>
</html>
```